CREATIVE, BEAUTIFUL, STANDOUT BUSINESS CARD WITH LOGO DESIRED

Hello. I am a screenwriter, going to Hollywood soon to seek representation by agents and managers, as well as to pitch my screenplays and TV scripts to producers.

I need a CREATIVE, BEAUTIFUL, STANDOUT ONE-SIDED business card and LOGO with the following features:

Marcus Pell
Screenwriter
--- This part ("Marcus Pell" on one line, and "Screenwriter" on the next) should be an enticing logo, for which I need a separate file, so that I can also use it for branding on my website, social media, etc.
Then, as part of the same text set, under my name and profession should be my contact information:
Phone: 555 - 214 - 7386
Email: marcuspell@[login to view URL]
Website: [login to view URL]

The second text set should contain the following:

LOGLINE: A brilliant, shrewd Hollywood visionary joins forces with a talented, prolific screenwriter to create wonderful stories and make lots of money together. Make this your story at www.marcuspellwrites.com.

With this message, I am uploading two attachments:

1. My photo
2. The text sets the card should contain.

You can use your design flair and creativity to work with layout, colors and design.

It should be dynamic and, when the recipient of the business card is sifting through the 60 or so cards they received that day, it should stand out and help them remember me, and make them want to reach out.

By entering this contest, you agree that, if you win, I will receive the source file for the business card, and the source file for the logo, so that I can make future changes, as well as the rights to them, so I can use the logo on my website, social media, advertising, etc.

Feel free to ask questions.

Thank you for your help, and good luck to you!

Marcus

```html
<!DOCTYPE html>
<html lang="en">
<head>
<meta charset="utf-8">
<title>Marcus Pell — Screenwriter Business Card</title>
<link rel="stylesheet" href="https://fonts.googleapis.com/css2?family=Open+Sans:wght@400;600;700&display=swap">
<style>
  :root {
    --backdrop: #2b2b2b;
    --card-red: #ec2550;
    --card-red-deep: #d81a43;
    --photo-warm: #8a5a3a;
    --photo-dark: #5a3a26;
    --ink-light: #ffffff;
    --band-dark: #2a2a2a;
  }
  * { margin: 0; padding: 0; box-sizing: border-box; }
  html, body {
    width: 1200px;
    height: 956px;
    overflow: hidden;
    background: var(--backdrop);
    font-family: "Open Sans", Arial, sans-serif;
  }
  .business-card {
    position: absolute;
    left: 370px;
    top: 88px;
    width: 460px;
    height: 780px;
    border-radius: 34px;
    overflow: hidden;
    background: linear-gradient(160deg, var(--card-red) 0%, var(--card-red-deep) 100%);
    color: var(--ink-light);
  }
  .card-art {
    position: absolute;
    inset: 0;
    width: 460px;
    height: 780px;
  }
  .brand-name {
    position: absolute;
    left: 150px;
    top: 352px;
    width: 290px;
    text-align: center;
    font-weight: 700;
    line-height: 1.1;
  }
  .brand-name .name { display: block; font-size: 38px; }
  .brand-name .role { display: block; font-size: 13px; letter-spacing: 5px; margin-top: 6px; }
  .contact-icons {
    position: absolute;
    left: 150px;
    top: 448px;
    width: 290px;
    display: flex;
    justify-content: center;
    gap: 8px;
  }
  .contact-icons svg { width: 26px; height: 26px; }
  .contact-list {
    position: absolute;
    left: 120px;
    top: 486px;
    width: 350px;
    text-align: center;
    font-size: 19px;
    line-height: 1;
  }
  .contact-list .phone { display: block; }
  .contact-list .website {
    display: inline-block;
    margin-top: 10px;
    padding: 5px 12px;
    background: var(--band-dark);
    font-size: 18px;
  }
  .contact-list .email { display: block; margin-top: 12px; }
  .divider {
    position: absolute;
    left: 40px;
    top: 604px;
    width: 390px;
    height: 1px;
    background: var(--ink-light);
  }
  .divider::after {
    content: "";
    position: absolute;
    left: 180px;
    top: -4px;
    width: 9px;
    height: 9px;
    border-radius: 50%;
    background: var(--ink-light);
  }
  .logline {
    position: absolute;
    left: 34px;
    top: 624px;
    width: 398px;
    font-size: 14.5px;
    line-height: 1.4;
    text-align: justify;
  }
</style>
</head>
<body>
  <div class="business-card">
    <svg class="card-art" viewBox="0 0 460 780" aria-hidden="false">
      <defs>
        <linearGradient id="portraitTone" x1="0" y1="0" x2="1" y2="1">
          <stop offset="0" stop-color="var(--photo-dark)"/>
          <stop offset="0.5" stop-color="var(--photo-warm)"/>
          <stop offset="1" stop-color="var(--photo-dark)"/>
        </linearGradient>
      </defs>
      <path role="img" aria-label="Portrait photo of the screenwriter"
            d="M0,0 H270 C300,90 290,230 210,285 C150,325 70,335 0,325 Z"
            fill="url(#portraitTone)"/>
      <path d="M286,0 C318,96 306,246 222,300 C160,340 72,350 0,340"
            fill="none" stroke="var(--ink-light)" stroke-width="3"/>
    </svg>

    <div class="brand-name">
      <span class="name">Marcus Pell</span>
      <span class="role">SCREENWRITER</span>
    </div>

    <div class="contact-icons">
      <svg viewBox="0 0 26 26" aria-label="Phone">
        <circle cx="13" cy="13" r="12" fill="var(--ink-light)"/>
        <path d="M9 7l2.5 3-1.5 1.5c1 2 2.5 3.5 4.5 4.5L16 14.5l3 2.5-1.5 2c-5 0-10-5-10-10z" fill="var(--card-red)"/>
      </svg>
      <svg viewBox="0 0 26 26" aria-label="Email">
        <circle cx="13" cy="13" r="12" fill="var(--ink-light)"/>
        <rect x="7" y="9" width="12" height="8" fill="var(--card-red)"/>
        <path d="M7 9l6 5 6-5" fill="none" stroke="var(--ink-light)" stroke-width="1.2"/>
      </svg>
      <svg viewBox="0 0 26 26" aria-label="Website">
        <circle cx="13" cy="13" r="12" fill="var(--ink-light)"/>
        <g fill="none" stroke="var(--card-red)" stroke-width="1.4">
          <circle cx="13" cy="13" r="6"/>
          <ellipse cx="13" cy="13" rx="2.6" ry="6"/>
          <path d="M7 13h12"/>
        </g>
      </svg>
    </div>

    <div class="contact-list">
      <span class="phone">555 - 214 - 7386</span>
      <span class="website">www.marcuspellwrites.com</span>
      <span class="email">marcuspell@marcuspellwrites.com</span>
    </div>

    <div class="divider"></div>

    <p class="logline">LOGLINE: A brilliant, shrewd Hollywood visionary joins forces with a talented, prolific screenwriter to create wonderful stories and make lots of money together. Make this your story at www.marcuspellwrites.com.</p>
  </div>
</body>
</html>
```